Luxury Business Card Design for High-End Window Treatments

Gilded Vantages
Custom Plantation Shutters & Architectural Shading Systems

⸻

BACK

Daniel Forsythe
Owner

Custom Interior & Exterior Window Treatments

919-482-7034
gildedvantages.com

I have included a picture that I’m hoping we can use on the back, but I’m also wondering if you can get rid of the ladder? Should we get rid of shutters , shades and blinds underneath Gilded Vantages?

Target Market(s)

High-end residential homeowners, custom home builders, architects, interior designers, and luxury renovation clients seeking premium plantation shutters and motorized architectural shading systems.

Industry/Entity Type

Custom Window treatments

Contact Information for Business Card

Front Gilded Vantages Custom Plantation Shutters Motorized Architectural Shading Systems BACK Daniel Forsythe Owner 919-482-7034 GildedVantages.com Custom Interior & Exterior Window Treatments By Appointment

Requirements
Nice to have
• Not 100% sure on nice to halves or the color but you can definitely check out my website to get a better understanding of what I’m trying to do

```html
<!DOCTYPE html>
<html lang="en">
<head>
<meta charset="utf-8">
<title>Gilded Vantages – Business Card</title>
<link href="https://fonts.googleapis.com/css2?family=Poppins:wght@400&family=Prata&display=swap" rel="stylesheet">
<style>
  :root {
    --backdrop: #9c9c9c;
    --card: #000000;
    --gold: #c9b152;
    --white: #ffffff;
    --photo-dark: #33373f;
    --photo-mid: #4a4e4f;
  }
  html, body {
    margin: 0;
    padding: 0;
    width: 1093px;
    height: 1200px;
    overflow: hidden;
    background: var(--backdrop);
  }
  .canvas {
    position: relative;
    width: 1093px;
    height: 1200px;
  }
  .card {
    position: absolute;
    left: 264px;
    width: 580px;
    height: 358px;
    background: var(--card);
    overflow: hidden;
    box-shadow: 3px 3px 4px rgba(0,0,0,0.45);
  }
  .card--contact { top: 226px; }
  .card--brand { top: 620px; }

  .contact-name {
    position: absolute;
    left: 27px;
    top: 36px;
    margin: 0;
    font-family: "Prata", serif;
    font-weight: 400;
    font-size: 25px;
    line-height: 1;
    color: var(--gold);
  }
  .contact-role {
    position: absolute;
    left: 27px;
    top: 63px;
    margin: 0;
    font-family: "Poppins", sans-serif;
    font-size: 17px;
    line-height: 1;
    color: var(--white);
  }
  .gold-rule {
    position: absolute;
    left: 27px;
    width: 36px;
    height: 2px;
    background: var(--gold);
  }
  .gold-rule--upper { top: 100px; }
  .gold-rule--lower { top: 214px; }

  .contact-list {
    position: absolute;
    left: 27px;
    top: 141px;
    margin: 0;
    padding: 0;
    list-style: none;
    font-family: "Poppins", sans-serif;
    font-size: 17px;
    line-height: 21px;
    color: var(--white);
  }
  .contact-list li {
    display: flex;
    align-items: center;
    gap: 7px;
  }
  .contact-icon { width: 17px; height: 17px; flex: none; }

  .contact-tagline {
    position: absolute;
    left: 27px;
    top: 242px;
    margin: 0;
    font-family: "Poppins", sans-serif;
    font-size: 17.3px;
    line-height: 21px;
    color: var(--gold);
  }

  .porch-photo {
    position: absolute;
    inset: 0;
    clip-path: polygon(369px 0, 580px 0, 580px 358px, 292px 358px);
    background: linear-gradient(160deg, var(--photo-mid) 0%, var(--photo-dark) 100%);
  }
  .gold-stripe {
    position: absolute;
    inset: 0;
    background: var(--gold);
    clip-path: polygon(334px 90px, 350px 90px, 292px 358px, 273px 358px);
  }

  .brand-name {
    position: absolute;
    left: 0;
    right: 0;
    top: 112px;
    margin: 0;
    text-align: center;
    font-family: "Prata", serif;
    font-weight: 400;
    font-size: 46px;
    line-height: 1;
    color: var(--gold);
  }
  .brand-rule {
    position: absolute;
    left: 53px;
    width: 477px;
    top: 255px;
    height: 2px;
    background: var(--gold);
  }
  .brand-tagline {
    position: absolute;
    left: 0;
    right: 0;
    top: 280px;
    margin: 0;
    text-align: center;
    font-family: "Prata", serif;
    font-size: 16px;
    line-height: 21px;
    letter-spacing: 0.3px;
    color: var(--gold);
  }
</style>
</head>
<body>
<main class="canvas">

  <section class="card card--contact">
    <h1 class="contact-name">Daniel Forsythe</h1>
    <p class="contact-role">Owner</p>
    <div class="gold-rule gold-rule--upper"></div>

    <ul class="contact-list">
      <li>
        <svg class="contact-icon" viewBox="0 0 24 24" aria-hidden="true">
          <path fill="#c9b152" d="M6.6 10.8c1.4 2.8 3.8 5.1 6.6 6.6l2.2-2.2c.3-.3.7-.4 1-.2 1.1.4 2.3.6 3.6.6.6 0 1 .4 1 1V20c0 .6-.4 1-1 1C10.6 21 3 13.4 3 4c0-.6.4-1 1-1h3.5c.6 0 1 .4 1 1 0 1.3.2 2.5.6 3.6.1.3 0 .7-.2 1z"/>
        </svg>
        <span>919-482-7034</span>
      </li>
      <li>
        <svg class="contact-icon" viewBox="0 0 24 24" aria-hidden="true">
          <path fill="#c9b152" d="M2 5h20v14H2z"/>
          <path fill="none" stroke="#000" stroke-width="1.6" d="M2.5 5.8 12 13l9.5-7.2M2.5 18.5l7-6M21.5 18.5l-7-6"/>
        </svg>
        <span>GildedVantages.com</span>
      </li>
    </ul>

    <div class="gold-rule gold-rule--lower"></div>

    <p class="contact-tagline">Custom Interior &amp; Exterior<br>Window Treatments<br>By Appointment</p>

    <div class="porch-photo" role="img" aria-label="Photo of a home's covered porch fitted with motorized exterior shades"></div>
    <div class="gold-stripe"></div>
  </section>

  <section class="card card--brand">
    <h2 class="brand-name">Gilded Vantages</h2>
    <div class="brand-rule"></div>
    <p class="brand-tagline">Gilded Vantages Custom<br>Plantation Shutters Motorized<br>Architectural Shading Systems</p>
  </section>

</main>
</body>
</html>
```